4R Capital business cards for a tech VC

We're starting a new Venture Capital that is focusing on bringing the best start ups from Israel to NYC
We need a business cards template for this that gives the sense of an entrepreneurial look
I don't want any religious signs on this even thought it's Israel
I'm looking for a techi feeling but not too crazy
The card should probably be in the same light blue as the logo and the logo in white

Target Market(s)

Investors

Industry/Entity Type

Tech

Contact Information for Business Card

The card needs to look slick and entrepreneurship like
The VC is focused on NYC and Tel Aviv so could be great to show something on the back side that is like NYC skyline or something like that
You can see the logo attached

Colors
0455a3
3276b5
85acd3
cedeed
eaf1f7

Requirements
Must have
• A very cool looking business card that shows we're a cutting edge tech VC with a focus on bringing start ups from Tel Aviv and leveraging the NYC ecosystem
Nice to have
• NYC skyline can be cool , maybe something that is connected to Tel Aviv

```html
<!DOCTYPE html>
<html lang="en">
<head>
<meta charset="utf-8">
<title>4R Capital — Business Cards</title>
<link rel="stylesheet" href="https://fonts.googleapis.com/css2?family=Montserrat:wght@400;700&display=swap">
<style>
  :root {
    --backdrop: #1b1b1b;
    --card-white: #ffffff;
    --brand-blue: #00a3dc;
    --deep-blue: #0a7cc1;
    --ink-blue: #0b6fb0;
  }
  * { box-sizing: border-box; margin: 0; padding: 0; }
  html, body {
    width: 1200px; height: 1000px; overflow: hidden;
    background: var(--backdrop);
    font-family: "Montserrat", sans-serif;
  }
  .card {
    position: absolute;
    width: 500px; height: 286px;
    overflow: hidden;
    box-shadow: 0 6px 18px rgba(0,0,0,.55);
  }

  /* Front */
  .card-front { left: 90px; top: 190px; background: var(--card-white); }
  .front-brand {
    position: absolute; left: 30px; top: 30px;
    font-weight: 700; font-size: 26px; color: var(--brand-blue);
    letter-spacing: .5px;
  }
  .accent-bar { position: absolute; width: 11px; }
  .accent-bar--upper { left: 305px; top: 0; height: 118px; background: var(--deep-blue); }
  .accent-bar--lower { left: 262px; top: 140px; height: 146px; background: var(--brand-blue); }
  .contact { position: absolute; left: 286px; top: 158px; color: var(--brand-blue); }
  .contact-name { font-weight: 700; font-size: 17px; color: var(--ink-blue); }
  .contact-role { font-size: 14px; margin-bottom: 12px; }
  .contact-line { font-size: 12px; line-height: 1.45; }

  /* Back */
  .card-back { left: 610px; top: 470px; background: var(--brand-blue); }
  .back-band { position: absolute; top: 126px; height: 16px; background: var(--card-white); }
  .back-band--left { left: 0; width: 120px; }
  .back-band--right { right: 0; width: 120px; }
  .back-brand {
    position: absolute; left: 0; right: 0; top: 110px;
    text-align: center;
    font-weight: 700; font-size: 40px; line-height: 48px;
    color: var(--card-white); letter-spacing: 1px;
  }
</style>
</head>
<body>
  <section class="card card-front" aria-label="Business card front">
    <div class="front-brand">4R Capital</div>
    <div class="accent-bar accent-bar--upper"></div>
    <div class="accent-bar accent-bar--lower"></div>
    <div class="contact">
      <p class="contact-name">John Doe</p>
      <p class="contact-role">Manager</p>
      <p class="contact-line">00 123 456 4568</p>
      <p class="contact-line">youremail@domain.com</p>
      <p class="contact-line">www.yoursite.com</p>
    </div>
  </section>

  <section class="card card-back" aria-label="Business card back">
    <div class="back-band back-band--left"></div>
    <div class="back-band back-band--right"></div>
    <div class="back-brand">4R Capital</div>
  </section>
</body>
</html>
```